Health and fitness directory/ blog website

We need a website design for a health focused website. The website will be advertising other health businesses via their directory page. The website should not be too fitness focused, as it needs a balance of health as well.

We want the website to be fun and colourful, while also staying clean and easy to use. The current logo is green, however we would like to utilize other colour schemes as well to make the website 'pop'

The font used should be helvetica for main content.

The client would like to see a design with complete creative freedom. They want something that represents 'vibrant/ energetic/ healthy/ fitness/ youthful' They want complete creative freedom with the design, including colours used and layout options (even the colour of the logo can change). They feel they have seen too many designs that look the same/ too similar from their brief and have not seen anything different/ haven't been given any alternative options. Maybe try a full width image/ large background/ oranges/ yellows/ greens/ helvetica font etc

The brief has been updated, please read and submit new designs.

Target Market(s)

Fitness and health enthusiasts - clean living reflected in a clean website. Women aged 18 - 40

Industry/Entity Type

Advertising

Font styles to use
Sans Serif

Requirements
Must have
• HEADER - - -
Navigation: Home/Trim Lass’s Journal/Zesty Plates/Style & Gear Stash/About Us/Contact Us/Sign Up Your Business

Rotating Banner - - -
Wording next to Picture: "The home of fitness, fashion and food inspiration." We then like the 'Join Now' which will lead to the newsletter sign up. Using the picture of the man next to the surfboard (included here).

CONTENT - - -
Blurb: h1: Welcome to Brightwell Living
p: So you want to get fit and healthy but don’t know where to go? We’ll help you. Find something that moves you through NZ’s biggest Fitness Directory below. The hardest part is choosing something and then you just have to turn up. Go on, give something a go!

We also want a directory search (keyword, select from categories, select from sub categories, select from region, select from sub region). It is important the search section stands out on the page.

We need 3 featured directory listings (from word document attached)

There needs to be space for an advert on the page.

FOOTER - - -
Can we please have going right across the page a simple sign up to our newsletter.
1) Tabs at bottom of page:
Brightwell Living Home/Trim Lass’s Journal//Zesty Plates/Style & Gear Stash/About Us/Contact Us/ Terms and Conditions / Privacy policy (these could go across two lines)
2) Join Us: Sign up your Business / Advertise with us
3) Get in touch: info@brightwellliving.co.nz / Follow Us (FB, Twitter, Instagram)
Nice to have

• An upcoming event section with a few upcoming race names/ dates/ locations listed. Would be nice, but not required.
Should not have
• No tacky submissions
not be too busy (needs to be a simple and clean design)
not have any extra social media icons other than the three listed.

No additional content sections, other than what is listed above

no "what our clients say" section

```html
<!DOCTYPE html>
<html lang="en">
<head>
<meta charset="utf-8">
<title>Brightwell Living</title>
<link href="https://fonts.googleapis.com/css2?family=Open+Sans:wght@400;600;700&family=Roboto:wght@400;700;900&display=swap" rel="stylesheet">
<style>
:root{
  --green:#00e02c;
  --green-dark:#18c93a;
  --ink:#1e1e1e;
  --text:#555;
  --muted:#8a8a8a;
  --line:#e2e2e2;
  --sky-top:#b8d4f4;
  --footer-bg:#eef0f4;
  --bar:#434343;
  --white:#fff;
}
*{box-sizing:border-box;margin:0;padding:0}
html,body{width:1200px;height:2368px;overflow:hidden}
body{position:relative;background:linear-gradient(#b7d3f3 0,#e6f0fb 180px,#fff 260px,#fff 100%);font-family:"Open Sans",Arial,sans-serif;color:var(--text)}
.abs{position:absolute}
.brand{left:0;width:1200px;top:34px;text-align:center}
.brand-mark{width:62px;height:62px;border-radius:50%;background:var(--green);margin:0 auto 8px}
.brand-name{font-size:38px;font-weight:400;color:#333;letter-spacing:1px;line-height:44px}
.nav{top:211px;left:137px;width:924px;display:flex;justify-content:space-between;font-size:13.5px;font-weight:600;color:var(--ink);letter-spacing:.3px;text-transform:uppercase}
.hero{top:245px;left:137px;width:924px;height:395px;background:linear-gradient(180deg,#8fb6dc 0%,#c9dcef 45%,#a9b58f 72%,#dad7c4 100%)}
.hero-card{top:311px;left:142px;width:532px;height:213px;background:rgba(255,255,255,.88);border-left:9px solid var(--green);padding:24px 26px}
.hero-title{font-family:Roboto,Arial,sans-serif;font-weight:900;font-size:33px;line-height:36px;color:var(--ink);letter-spacing:-.5px}
.hero-title span{display:block;color:var(--green);font-weight:700}
.hero-text{font-size:11.5px;line-height:17px;color:#666;margin:8px 0 18px;width:470px}
.btn-dark{display:inline-block;background:#222;color:#fff;font-size:12px;font-weight:600;text-transform:uppercase;padding:9px 32px;border-radius:2px}
.section-head{left:137px;width:924px;display:flex;align-items:center;gap:22px}
.section-head::before,.section-head::after{content:"";flex:1;height:1px;background:var(--line)}
.section-head h2{font-weight:600;font-size:22px;color:#222;text-transform:uppercase;letter-spacing:.5px;white-space:nowrap}
.section-head.light h2{font-weight:400}
.welcome-text{top:720px;left:147px;width:904px;text-align:center;font-size:15.5px;line-height:23px;color:#8c8c8c}
.search{top:812px;left:137px;width:924px;height:153px;background:var(--green)}
.search h3{position:absolute;top:30px;width:100%;text-align:center;font-size:22px;font-weight:600;color:#10331a;letter-spacing:.4px;text-transform:uppercase}
.search-row{position:absolute;top:82px;left:13px;display:flex;gap:6px}
.field{height:35px;background:#fff;border-radius:2px;font-size:11px;color:#aaa;padding:0 8px;display:flex;align-items:center;justify-content:space-between}
.field i{width:14px;height:14px;border:1px solid #ccc;font-style:normal;font-size:8px;display:flex;align-items:center;justify-content:center;color:#999}
.btn-search{width:139px;height:35px;background:#222;color:#fff;font-weight:700;font-size:14px;display:flex;align-items:center;justify-content:center;margin-left:3px}
.card{top:1118px;width:280px;height:520px;background:#fff;border:1px solid #dcdcdc;box-shadow:0 1px 3px rgba(0,0,0,.05)}
.card-badge{position:absolute;top:-56px;left:77px;width:126px;height:126px;border-radius:50%;background:#fff;border:1px solid #e5e5e5;display:flex;align-items:center;justify-content:center}
.card-badge span{width:86px;height:86px;border-radius:50%;background:#e9ecef}
.card h4{position:absolute;top:95px;width:100%;text-align:center;font-size:14.5px;font-weight:600;color:#222;text-transform:uppercase}
.card-body{position:absolute;top:143px;left:20px;width:240px;text-align:center;font-size:12px;line-height:16.5px;color:#666}
.card-body p+p{margin-top:8px}
.rating{position:absolute;top:310px;left:0;width:100%;height:39px;background:#e6e6e6;display:flex;align-items:center;justify-content:space-between;padding:0 16px;font-size:15px;color:#333}
.rating::after{content:"";position:absolute;bottom:-8px;left:132px;border:8px solid transparent;border-top-color:#e6e6e6;border-bottom:0}
.stars{display:flex;gap:3px}
.count{display:flex;align-items:center;gap:6px}
.contacts{position:absolute;top:368px;left:17px;list-style:none;font-size:12.5px;color:#555}
.contacts li{display:flex;align-items:center;gap:10px;height:37px}
.contacts li.hl{color:var(--green-dark)}
.advert{top:1675px;left:137px;width:924px;height:180px;background:linear-gradient(90deg,#4d7fc4 0%,#8bb6e4 45%,#d3e3f3 75%,#b4cd8a 100%)}
.advert p{position:absolute;color:#fff;font-family:Roboto,Arial,sans-serif;font-size:38px;text-shadow:0 1px 3px rgba(0,0,0,.3)}
.footer{top:1890px;left:0;width:1200px;height:428px;background:var(--footer-bg)}
.newsletter{top:1936px;left:150px;display:flex;gap:10px}
.newsletter .in{width:318px;height:40px;background:#fff;border:1px solid #d8d8d8;font-size:11.5px;color:#aaa;padding:0 12px;display:flex;align-items:center;text-transform:uppercase}
.newsletter .btn-green{width:234px;height:40px;margin-left:12px;background:var(--green);color:#fff;font-weight:700;font-size:14px;display:flex;align-items:center;justify-content:center;text-transform:uppercase}
.divider{top:2020px;left:150px;width:900px;height:1px;background:#e0e2e6;box-shadow:0 3px 6px rgba(0,0,0,.05)}
.fcol{top:2080px}
.fcol h5{font-size:12px;font-weight:600;color:#222;text-transform:uppercase;display:flex;align-items:center;gap:10px;margin-bottom:12px}
.fcol h5::after{content:"";width:80px;height:1px;background:#d6d6d6}
.fcol ul{list-style:none;font-size:11.5px;color:#777}
.fcol li{height:22px;display:flex;align-items:center;gap:10px}
.fcol li::before{content:"";width:6px;height:6px;border-radius:50%;border:1px solid #bbb}
.touch{top:2080px;left:886px;width:180px}
.touch h5{font-size:12px;font-weight:600;color:#222;text-transform:uppercase;margin-bottom:14px}
.phone{font-size:17px;color:#555;display:flex;align-items:center;gap:8px;letter-spacing:.5px}
.mail{font-size:11.5px;color:var(--green-dark);display:flex;align-items:center;gap:8px;margin-top:6px;padding-bottom:10px;border-bottom:1px solid #d6d6d6}
.follow{top:2199px;left:886px;width:180px;text-align:right;font-size:12px;font-weight:600;color:#222;text-transform:uppercase}
.social{top:2232px;left:940px;display:flex;gap:8px}
.social span{width:30px;height:30px;border-radius:50%;background:#3b3b3b}
.bottom-bar{top:2318px;left:0;width:1200px;height:50px;background:var(--bar);color:#eee;font-size:12px;display:flex;align-items:center;justify-content:space-between;padding:0 150px}
</style>
</head>
<body>

<div class="abs brand">
  <div class="brand-mark"></div>
  <div class="brand-name">BRIGHTWELL LIVING</div>
</div>

<nav class="abs nav">
  <span>Home</span><span>Trim Lass’s Journal</span><span>Zesty Plates</span><span>Style &amp; Gear Stash</span><span>About Us</span><span>Contact Us</span><span>Sign Up Your Business</span>
</nav>

<div class="abs hero" role="img" aria-label="Photo of a man balancing in a yoga pose beside a surfboard on a beach under a blue sky"></div>
<div class="abs hero-card">
  <div class="hero-title">EVERYTHING YOU NEED TO GET<span>THE RESULTS YOU WANTS</span></div>
  <p class="hero-text">So you want to get fit and healthy but don’t know where to go? We’ll help. Just find something that moves you through NZ’s biggest Fitness Directory below.</p>
  <span class="btn-dark">Join Now!</span>
</div>

<div class="abs section-head" style="top:673px"><h2>Welcome to Brightwell Living</h2></div>
<p class="abs welcome-text">So you want to get fit and healthy but don’t know where to go? We’ll help. Just find something that moves you through NZ’s biggest Fitness Directory below. You’re sure to find something in your backyard. Go on, give something a go!</p>

<section class="abs search">
  <h3>Search a Fitness Idea Here</h3>
  <div class="search-row">
    <div class="field" style="width:249px">Enter your Key world</div>
    <div class="field" style="width:119px">Category<i>▼</i></div>
    <div class="field" style="width:119px">Sub Category<i>▼</i></div>
    <div class="field" style="width:119px">Region<i>▼</i></div>
    <div class="field" style="width:119px">Sub Region<i>▼</i></div>
    <div class="btn-search">SEARCH</div>
  </div>
</section>

<div class="abs section-head light" style="top:995px"><h2>Featured Listings</h2></div>

<svg width="0" height="0" style="position:absolute">
  <defs>
    <symbol id="star" viewBox="0 0 20 20"><path d="M10 1l2.6 6 6.4.5-4.9 4.2 1.5 6.3L10 14.7 4.4 18l1.5-6.3L1 7.5l6.4-.5z"/></symbol>
    <symbol id="half" viewBox="0 0 20 20"><path d="M10 1v13.7L4.4 18l1.5-6.3L1 7.5l6.4-.5z" fill="#1fc93c"/><path d="M10 1l2.6 6 6.4.5-4.9 4.2 1.5 6.3L10 14.7 4.4 18l1.5-6.3L1 7.5l6.4-.5z" fill="none" stroke="#333" stroke-width="1.3"/></symbol>
    <symbol id="empty" viewBox="0 0 20 20"><path d="M10 1l2.6 6 6.4.5-4.9 4.2 1.5 6.3L10 14.7 4.4 18l1.5-6.3L1 7.5l6.4-.5z" fill="none" stroke="#333" stroke-width="1.3"/></symbol>
    <symbol id="bubble" viewBox="0 0 20 20"><path d="M3 4h14v9H9l-4 3v-3H3z" fill="none" stroke="#333" stroke-width="1.8" stroke-linejoin="round"/></symbol>
    <symbol id="home" viewBox="0 0 20 20"><path d="M2 10l8-7 8 7M5 8v9h10V8" fill="none" stroke="#333" stroke-width="1.8"/></symbol>
    <symbol id="phone" viewBox="0 0 20 20"><rect x="3" y="2" width="14" height="16" rx="2" fill="none" stroke="#333" stroke-width="1.8"/><path d="M6 6h8M6 10h8M6 14h8" stroke="#333" stroke-width="1.5"/></symbol>
    <symbol id="mail" viewBox="0 0 20 20"><rect x="2" y="4" width="16" height="12" fill="none" stroke="#333" stroke-width="1.8"/><path d="M2 5l8 6 8-6" fill="none" stroke="#333" stroke-width="1.6"/></symbol>
    <symbol id="globe" viewBox="0 0 20 20"><circle cx="10" cy="10" r="8" fill="none" stroke="#333" stroke-width="1.7"/><ellipse cx="10" cy="10" rx="3.5" ry="8" fill="none" stroke="#333" stroke-width="1.4"/><path d="M2 10h16" stroke="#333" stroke-width="1.4"/></symbol>
    <symbol id="handset" viewBox="0 0 20 20"><path d="M5 2l3 4-2 2c1 2.5 3 4.5 6 6l2-2 4 3-2 3C9 18 2 11 2 4z" fill="none" stroke="#777" stroke-width="1.5" stroke-linejoin="round"/></symbol>
  </defs>
</svg>

<article class="abs card" style="left:152px">
  <div class="card-badge"><span></span></div>
  <h4>Core Motion Studio</h4>
  <div class="card-body">
    <p>Hana is a Personal Trainer, with her own private, spacious studio located in central Auckland, with ample parking.</p>
    <p>Hana is highly motivated to help you reach your goals.</p>
    <p>Sessions can be one-on-one PT sessions, or group sessions of two up to 8</p>
  </div>
  <div class="rating">
    <div class="stars"><svg width="15" height="15" fill="#1fc93c"><use href="#star"/></svg><svg width="15" height="15" fill="#1fc93c"><use href="#star"/></svg><svg width="15" height="15" fill="#1fc93c"><use href="#star"/></svg><svg width="15" height="15"><use href="#half"/></svg><svg width="15" height="15"><use href="#empty"/></svg></div>
    <div class="count"><svg width="18" height="18"><use href="#bubble"/></svg>120</div>
  </div>
  <ul class="contacts">
    <li><svg width="17" height="17"><use href="#home"/></svg>12 Harbour Lane, Auckland,</li>
    <li><svg width="17" height="17"><use href="#phone"/></svg>021 555 018</li>
    <li><svg width="17" height="17"><use href="#mail"/></svg>hana@coremotion.kiwi</li>
    <li><svg width="17" height="17"><use href="#globe"/></svg>www.coremotion.kiwi</li>
  </ul>
</article>

<article class="abs card" style="left:460px">
  <div class="card-badge"><span></span></div>
  <h4>StrideWell</h4>
  <div class="card-body">
    <p>StrideWell provides Run training groups based in Auckland plus one on one coaching services throughout New Zealand. We also provide full and half marathon tours Domestically and Internationally visiting marathons such as Paris, London, N.Y &amp;Melb.</p>
  </div>
  <div class="rating">
    <div class="stars"><svg width="15" height="15" fill="#1fc93c"><use href="#star"/></svg><svg width="15" height="15" fill="#1fc93c"><use href="#star"/></svg><svg width="15" height="15" fill="#1fc93c"><use href="#star"/></svg><svg width="15" height="15"><use href="#half"/></svg><svg width="15" height="15"><use href="#empty"/></svg></div>
    <div class="count"><svg width="18" height="18"><use href="#bubble"/></svg>120</div>
  </div>
  <ul class="contacts">
    <li><svg width="17" height="17"><use href="#home"/></svg>7 Kowhai Street, Grafton</li>
    <li class="hl"><svg width="17" height="17"><use href="#phone"/></svg>09 555 0143</li>
    <li><svg width="17" height="17"><use href="#mail"/></svg>info@stridewell.co.nz</li>
    <li><svg width="17" height="17"><use href="#globe"/></svg>www.stridewell.co.nz</li>
  </ul>
</article>

<article class="abs card" style="left:767px">
  <div class="card-badge"><span></span></div>
  <h4>Peak Kit Room</h4>
  <div class="card-body">
    <p>Peak Kit Room is a source of coaching services that will enhance one’s health &amp; wellness, and performance efficiency. Our speciality is triathlon and duathlon, ranging from sprint to long distance, both on and off road. We also cater for runners and mountain bikers.</p>
  </div>
  <div class="rating">
    <div class="stars"><svg width="15" height="15" fill="#1fc93c"><use href="#star"/></svg><svg width="15" height="15" fill="#1fc93c"><use href="#star"/></svg><svg width="15" height="15" fill="#1fc93c"><use href="#star"/></svg><svg width="15" height="15"><use href="#half"/></svg><svg width="15" height="15"><use href="#empty"/></svg></div>
    <div class="count"><svg width="18" height="18"><use href="#bubble"/></svg>120</div>
  </div>
  <ul class="contacts">
    <li><svg width="17" height="17"><use href="#home"/></svg>12 Harbour Lane, Auckland,</li>
    <li><svg width="17" height="17"><use href="#phone"/></svg>021 555 0291</li>
    <li><svg width="17" height="17"><use href="#mail"/></svg>marcus@peakkitroom.co.nz</li>
    <li><svg width="17" height="17"><use href="#globe"/></svg>www.peakkitroom.co.nz</li>
  </ul>
</article>

<div class="abs advert" role="img" aria-label="Advert photo of a family playing together outdoors on a sunny day">
  <p style="left:36px;top:50px">Health Insurance</p>
  <p style="left:115px;top:110px">For Your Family</p>
</div>

<div class="abs footer"></div>

<div class="abs newsletter">
  <div class="in">Your Full Name:</div>
  <div class="in">Your Email Address:</div>
  <div class="btn-green">Get Our Newsletter</div>
</div>
<div class="abs divider"></div>

<div class="abs fcol" style="left:150px">
  <h5>Brightwell Living</h5>
  <ul><li>Home</li><li>Trim Lass’s Journal</li><li>Zesty Plates</li><li>Style &amp; Gear Stash</li><li>About Us</li><li>Contact Us</li><li>Terms and Conditions</li><li>Privacy policy</li></ul>
</div>
<div class="abs fcol" style="left:396px">
  <h5>Customers Services</h5>
  <ul><li>Lorem Ipsum Is That It</li><li>Has A More-or-less</li><li>Normal Distribution Of</li><li>Letters, as Opposed To</li><li>Using 'Content Here,</li><li>Content Here', Making It</li><li>Look Like Readable</li></ul>
</div>
<div class="abs fcol" style="left:669px">
  <h5>Join Us</h5>
  <ul><li>Sign up your Business</li><li>Advertise with us</li></ul>
</div>
<div class="abs touch">
  <h5>Get in Touch</h5>
  <div class="phone"><svg width="16" height="16"><use href="#handset"/></svg>123 - 555 - 0147</div>
  <div class="mail"><svg width="15" height="15"><use href="#mail"/></svg>info@brightwellliving.co.nz</div>
</div>
<div class="abs follow">Follow Us:</div>
<div class="abs social" aria-label="Social links"><span></span><span></span><span></span></div>

<div class="abs bottom-bar">
  <span>Copyright © 2014 Brightwell Living - All Rights Reserved.</span>
  <span>website by Site Craft Studio.</span>
</div>

</body>
</html>
```